Business Card Design Project

Hello,

We have just created our new COMPANY LOGO via Fenwick Loom and would not like to turn our attention to new Business Cards.

We are a printing company based in Singapore & Las Vegas. We specialize in blue-print printing for the Architectural, Engineering and Construction industries

The design should be simple, professional, clean and organized.

The Business Cards should "pop" when seen and will hopefully be something that makes you look twice.

We have two different Pan-tones that we use for our company, feel free to use them if you think they will work for your design?

Orange: PMS 021
Gray: PMS 431

I have attached our current logo for your use and reference which should obvious be on our business cards.

Considering we have two locations on different continents, we need business cards templates where the address details need to be interchangeable for each different location (total 2)

First one:
42 Mereton Road #03-11 to #03-15
Singapore 512847
Tel : +65 6483-2207
Fax : +65 6487-9042

Second one:
3218 W. Larkspur Blvd, Suite 204
Las Vegas, Nevada 89147
Tel : (702) 555-0143
Fax : (702) 555-0178

We would also like to list a few of our key services on the card. Here are a few examples to get you going.

Plan Printing & Plotting
Digital Colour Printing
Cadline Printing
Specialty Book Making
Scanning & Archiving
Collection & Delivey

This is the first time i have requested for business cards to be created so please let me know if you require any additional information.
Many Thanks,
Tomas
Updates

Reason: It took us longer than expected to finalize our Company Logo We look forward to receiving your designs.

Target Market(s)

Our Target Market is construction related people.
Construction
Architecture
Engineering

Industry/Entity Type

Printing

Font styles to use
Other font styles liked:
• Times New Roman

Colors
faa54b
ffffff

Requirements
Must have
• The business card must have our Company Logo (attached)
The font used must be Times New Roman
Should not have
• Playful images of print designs and/or logos

```html
<!DOCTYPE html>
<html lang="en">
<head>
<meta charset="utf-8">
<title>Halvern Print Solutions – Business Cards</title>
<link rel="stylesheet" href="https://fonts.googleapis.com/css2?family=Tinos:ital,wght@0,400;0,700;1,400;1,700&display=swap">
<style>
  :root{
    --page:#ececec;
    --orange-deep:#f05a28;
    --orange-soft:#f8a54b;
    --white:#ffffff;
    --ink:#111111;
    --card-shadow:0 6px 18px rgba(0,0,0,.22);
  }
  *{box-sizing:border-box;margin:0;padding:0}
  html,body{width:1037px;height:1200px;overflow:hidden}
  body{background:var(--page);font-family:"Tinos","Times New Roman",serif;color:var(--ink);position:relative}

  .card{position:absolute;width:480px;height:274px;box-shadow:var(--card-shadow);overflow:hidden}
  .row-sg{top:230px}
  .row-lv{top:660px}
  .col-front{left:26px}
  .col-back{left:531px}

  /* Front face */
  .card-front{background:var(--orange-deep)}
  .card-front .edge{position:absolute;left:0;right:0;height:6px;background:var(--ink)}
  .card-front .edge-top{top:0}
  .card-front .edge-bottom{bottom:0}
  .card-front .brand{position:absolute;top:62px;left:0;right:0;text-align:center}
  .services{position:absolute;left:0;right:0;bottom:18px;height:50px;background:var(--white);
    display:flex;flex-direction:column;justify-content:center;align-items:center;gap:5px;font-size:11px}
  .services ul{list-style:none;display:flex}
  .services li{padding:0 8px;border-left:1px solid var(--ink);line-height:1}
  .services li:first-child{border-left:none}

  /* Brand block */
  .wordmark{font-weight:700;font-size:38px;letter-spacing:1px;line-height:1;color:var(--ink)}
  .brand-name{font-weight:700;font-size:18px;margin-top:8px}
  .brand-tagline{font-weight:700;font-style:italic;font-size:12.5px;margin-top:2px}

  /* Contact face */
  .card-back{background:var(--white);display:flex}
  .card-back .brand-panel{width:48%;background:var(--orange-soft);display:flex;flex-direction:column;
    justify-content:center;align-items:center;text-align:center}
  .card-back .wordmark{font-size:32px}
  .card-back .brand-name{font-size:14.5px;margin-top:6px}
  .card-back .brand-tagline{font-size:9.5px}
  .details{flex:1;padding:68px 0 0 20px}
  .person-name{font-weight:700;font-size:15.5px}
  .person-role{font-style:italic;font-size:9.5px;margin-top:2px}
  .contacts{list-style:none;margin-top:28px;font-size:11.5px}
  .contacts li{display:flex;align-items:flex-start;gap:10px;margin-bottom:8px;line-height:1.3}
  .contacts svg{width:13px;height:13px;flex:none;margin-top:1px}
</style>
</head>
<body>
<svg width="0" height="0" style="position:absolute" aria-hidden="true">
  <defs>
    <symbol id="icon-phone" viewBox="0 0 16 16">
      <rect x="0.5" y="0.5" width="15" height="15" fill="none" stroke="#111"/>
      <path d="M3 6 Q8 2 13 6 L12 7.5 L10 6.5 L6 6.5 L4 7.5 Z" fill="#111"/>
      <rect x="4.5" y="8" width="7" height="5" fill="#111"/>
    </symbol>
    <symbol id="icon-fax" viewBox="0 0 16 16">
      <rect x="0.5" y="0.5" width="15" height="15" fill="#111"/>
      <rect x="4" y="3" width="8" height="4" fill="#fff"/>
      <rect x="3" y="8" width="10" height="5" fill="#fff"/>
      <rect x="5" y="10" width="6" height="1" fill="#111"/>
    </symbol>
    <symbol id="icon-mail" viewBox="0 0 16 16">
      <rect x="0.5" y="0.5" width="15" height="15" fill="none" stroke="#111"/>
      <rect x="3" y="4.5" width="10" height="7" fill="none" stroke="#111"/>
      <path d="M3 4.5 L8 9 L13 4.5" fill="none" stroke="#111"/>
    </symbol>
    <symbol id="icon-home" viewBox="0 0 16 16">
      <rect x="0.5" y="0.5" width="15" height="15" fill="#111"/>
      <path d="M8 3 L13 8 L11.5 8 L11.5 13 L4.5 13 L4.5 8 L3 8 Z" fill="#fff"/>
      <rect x="7" y="10" width="2" height="3" fill="#111"/>
    </symbol>
  </defs>
</svg>

<!-- Singapore set -->
<section class="card card-front row-sg col-front">
  <div class="edge edge-top"></div>
  <div class="brand">
    <div class="wordmark">Halvern</div>
    <div class="brand-name">Halvern Print Solutions</div>
    <div class="brand-tagline">A Member of the Halvern Group of Companies</div>
  </div>
  <div class="services">
    <ul><li>Plan Printing &amp; Plotting</li><li>Digital Colour Printing</li><li>Cadline Printing</li><li>Specialty Book Making</li></ul>
    <ul><li>Scanning &amp; Archiving</li><li>Collection &amp; Delivey</li></ul>
  </div>
  <div class="edge edge-bottom"></div>
</section>

<section class="card card-back row-sg col-back">
  <div class="brand-panel">
    <div class="wordmark">Halvern</div>
    <div class="brand-name">Halvern Print Solutions</div>
    <div class="brand-tagline">A Member of the Halvern Group of Companies</div>
  </div>
  <div class="details">
    <div class="person-name">Marcus Ellery</div>
    <div class="person-role">Managing Director</div>
    <ul class="contacts">
      <li><svg><use href="#icon-phone"/></svg>+65 6483-2207</li>
      <li><svg><use href="#icon-fax"/></svg>+65 6487-9042</li>
      <li><svg><use href="#icon-mail"/></svg>hello@halvernprint.com</li>
      <li><svg><use href="#icon-home"/></svg><span>42 Mereton Road #03-11 to #03-15<br>Singapore 512847</span></li>
    </ul>
  </div>
</section>

<!-- Las Vegas set -->
<section class="card card-front row-lv col-front">
  <div class="edge edge-top"></div>
  <div class="brand">
    <div class="wordmark">Halvern</div>
    <div class="brand-name">Halvern Print Solutions</div>
    <div class="brand-tagline">A Member of the Halvern Group of Companies</div>
  </div>
  <div class="services">
    <ul><li>Plan Printing &amp; Plotting</li><li>Digital Colour Printing</li><li>Cadline Printing</li><li>Specialty Book Making</li></ul>
    <ul><li>Scanning &amp; Archiving</li><li>Collection &amp; Delivey</li></ul>
  </div>
  <div class="edge edge-bottom"></div>
</section>

<section class="card card-back row-lv col-back">
  <div class="brand-panel">
    <div class="wordmark">Halvern</div>
    <div class="brand-name">Halvern Print Solutions</div>
    <div class="brand-tagline">A Member of the Halvern Group of Companies</div>
  </div>
  <div class="details">
    <div class="person-name">Priya Solden</div>
    <div class="person-role">Managing Director</div>
    <ul class="contacts">
      <li><svg><use href="#icon-phone"/></svg>(702) 555-0143</li>
      <li><svg><use href="#icon-fax"/></svg>(702) 555-0178</li>
      <li><svg><use href="#icon-mail"/></svg>hello@halvernprint.com</li>
      <li><svg><use href="#icon-home"/></svg><span>3218 W. Larkspur Blvd, Suite 204<br>Las Vegas, Nevada 89147</span></li>
    </ul>
  </div>
</section>
</body>
</html>
```